Commercial photographer, UAV drone photography & 360 walk-through visuals

I need a business card design that is minimalist but yet pretentiously creative. My target market are architects, designers, advertising agents and marketing managers. It is important to stress that though I am asking for a minimalist design it needs to have creative impact.

Target Market(s)

Architects, interiors designers, web-designers, artists

Contact Information for Business Card

Include my name, mobile [cell] number, email, web page and the company logo. Do not to include a postal address.

Colors

Designer to choose colors to be used in the design.

Requirements
Must have
• The following information is to be included:
• Miles Perrow
• Photographer
• m: 07812 593174
• e: miles@mpframeworks.co.uk
• w: mpframeworks.co.uk

```html
<!DOCTYPE html>
<html lang="en">
<head>
<meta charset="utf-8">
<title>MP Frameworks — Business Card</title>
<link href="https://fonts.googleapis.com/css2?family=Montserrat:wght@400;600&family=Open+Sans:wght@400&display=swap" rel="stylesheet">
<style>
  :root {
    --backdrop: #2b2b2d;
    --card: #1f1f20;
    --card-edge: #2a2a2b;
    --ink: #ffffff;
    --ink-soft: #d8d8d8;
    --mark: #bdbdbd;
  }
  * { margin: 0; padding: 0; box-sizing: border-box; }
  html, body {
    width: 1200px;
    height: 895px;
    overflow: hidden;
    background: var(--backdrop);
  }
  .stage {
    position: relative;
    width: 1200px;
    height: 895px;
  }
  .card {
    position: absolute;
    left: 260px;
    width: 680px;
    height: 390px;
    border-radius: 22px;
    background: var(--card);
    border: 1px solid var(--card-edge);
    box-shadow: 0 14px 30px rgba(0,0,0,0.45);
    overflow: hidden;
  }
  .card--front { top: 40px; }
  .card--back  { top: 465px; }

  .brand {
    position: absolute;
    font-family: "Montserrat", sans-serif;
    font-weight: 400;
    color: var(--ink);
    text-transform: uppercase;
    letter-spacing: 0.08em;
    line-height: 1.05;
  }
  .brand__line { display: block; }

  /* Front: large plain disc upper right, stacked name lower left */
  .front__disc {
    position: absolute;
    right: 110px;
    top: 48px;
    width: 200px;
    height: 200px;
    border-radius: 50%;
    background: var(--mark);
  }
  .card--front .brand {
    left: 56px;
    bottom: 52px;
    font-size: 46px;
  }

  /* Back */
  .card--back .brand {
    right: 52px;
    top: 42px;
    font-size: 30px;
    text-align: left;
  }

  .person {
    position: absolute;
    left: 300px;
    top: 150px;
    font-family: "Montserrat", sans-serif;
    color: var(--ink);
  }
  .person__name {
    font-weight: 600;
    font-size: 24px;
    letter-spacing: 0.06em;
    text-transform: uppercase;
  }
  .person__role {
    font-family: "Open Sans", sans-serif;
    font-size: 15px;
    color: var(--ink-soft);
    margin-top: 4px;
    letter-spacing: 0.04em;
  }

  .contact {
    position: absolute;
    left: 48px;
    top: 200px;
    font-family: "Open Sans", sans-serif;
    color: var(--ink);
  }
  .contact__icons {
    display: flex;
    gap: 12px;
    margin-bottom: 10px;
  }
  .contact__icons svg { width: 18px; height: 18px; }
  .contact__phone {
    font-size: 24px;
    letter-spacing: 0.06em;
  }
  .contact__email {
    font-size: 16px;
    margin-top: 6px;
    color: var(--ink-soft);
  }
  .contact__rule {
    width: 64px;
    height: 2px;
    background: var(--ink);
    margin: 14px 0 12px;
  }
  .contact__web {
    font-size: 16px;
    color: var(--ink-soft);
  }
</style>
</head>
<body>
<main class="stage">
  <section class="card card--front" aria-label="Card front">
    <span class="front__disc"></span>
    <p class="brand">
      <span class="brand__line">MP</span>
      <span class="brand__line">Frameworks</span>
    </p>
  </section>

  <section class="card card--back" aria-label="Card back">
    <p class="brand">
      <span class="brand__line">MP</span>
      <span class="brand__line">Frameworks</span>
    </p>

    <div class="person">
      <p class="person__name">Miles Perrow</p>
      <p class="person__role">Photographer</p>
    </div>

    <div class="contact">
      <div class="contact__icons">
        <svg viewBox="0 0 24 24" aria-label="Phone">
          <path fill="#ffffff" d="M6.6 10.8a15.1 15.1 0 0 0 6.6 6.6l2.2-2.2c.3-.3.7-.4 1-.2 1.1.4 2.3.6 3.6.6.6 0 1 .4 1 1V20c0 .6-.4 1-1 1A17 17 0 0 1 3 4c0-.6.4-1 1-1h3.5c.6 0 1 .4 1 1 0 1.3.2 2.5.6 3.6.1.3 0 .7-.2 1z"/>
        </svg>
        <svg viewBox="0 0 24 24" aria-label="Email">
          <rect x="2" y="5" width="20" height="14" rx="1.5" fill="#ffffff"/>
          <path d="M3 6.5l9 6.5 9-6.5" fill="none" stroke="#1f1f20" stroke-width="1.8"/>
        </svg>
      </div>
      <p class="contact__phone">07812 593174</p>
      <p class="contact__email">miles@mpframeworks.co.uk</p>
      <div class="contact__rule"></div>
      <p class="contact__web">www.mpframeworks.co.uk</p>
    </div>
  </section>
</main>
</body>
</html>
```